Ready to be wowed! Snazzy, sassy, classy Realtor seeking Web banner for unique innovative Realtor!

Placer County Realtor need web banner re-design. Looking for classy, classic, clean design appealing to elite prospects. Previous focus was short sales now looking to gear towards listing and selling homes, remove short sale focus. Must include, license # 04729318, HR logo, phone, email, etc. check out LiaPorter.com for reference info. I am open to suggestions for other needed content for THE BEST WEB BANNER ON EARTH! LOL. I really want to appeal to the upscale clients, also will be getting away from orange colors going more to a green. Please contact me at LiaPorterSells@mailvista.com for more info
measurements of banner; Images of exactly 960 × 120 pixels will be used as-is. It's Wordpress Genesis.
Updates

I'm really looking for something clean that looks upscale and luxury, classy. 

Please update email address to lia@liaporter.com

Reason: I still haven't gotten what I want. I noticed some really good designs closer to the end here, I'm hoping to allow those folks and maybe a few new ones the opportunity to give me exactly what I want! Thanks!

Reason: I still don't have what I want. I want a simple design that shows that I am a Realtor, maybe a picture of a house???? or something related to real estate. Less emphasis on the Halverson Realty logo. Classy and upscale. Fonts should be easy to read but not so simply boring. Please, please, please read the brief!! I REALLY want a good banner!!

Please take a look at the site color adjustment. That's what color it will stay. www.LiaPorter.com

Reason: I'm ready to move this to the end now. I need a design. I'm extending hopefully only this last time to take a vote on them. I will be reaching out to a few select designers to make a few modifications. I appreciate everyone's time on this as you know this is a very tough and important decision to make.

Reason: Need more input

Reason: still trying to decide

Target Market(s)

upscale home sellers

Industry/Entity Type

Realtor

Requirements
Must have
• License # 04729318
Phone (555)304-2871
HR LOGO (attached)
areas of service- Roseville, Rocklin, Granite Bay
LiaPorterSells@mailvista.com

```html
<!DOCTYPE html>
<html lang="en">
<head>
<meta charset="utf-8">
<title>Lia Porter Real Estate</title>
<link rel="stylesheet" href="https://fonts.googleapis.com/css2?family=Archivo:wght@800&family=Titillium+Web:wght@400;600;700&display=swap">
<style>
:root{
  --page:#2b2a29;
  --green:#5a8a3c;
  --green-dark:#4a7a30;
  --green-text:#5c9a2e;
  --navy:#1f3a8a;
  --ink:#2a2a2a;
  --muted:#a9a9a9;
  --nav:#bdbdbd;
  --band-dark:#2f2e2d;
  --tan:#f1dcaa;
  --card-gap:#e6e6e6;
  --white:#ffffff;
  --icon:#dfe4f2;
}
*{box-sizing:border-box;margin:0;padding:0}
html,body{width:1200px;height:960px;overflow:hidden;background:var(--page)}
body{position:relative;font-family:"Titillium Web",sans-serif}
.site{position:absolute;left:19.5px;top:15px;width:774px;height:620px;transform:scale(1.5);transform-origin:0 0;overflow:hidden}

.banner{position:absolute;left:0;top:0;width:774px;height:96px}
.banner svg{position:absolute;inset:0}
.houses{position:absolute;left:25px;top:6px;width:215px;height:62px;background:linear-gradient(180deg,rgba(40,60,30,.18),rgba(40,60,30,.05))}
.areas-label{position:absolute;left:283px;top:5px;font-size:12px;line-height:14px;color:var(--navy)}
.area{position:absolute;font-family:"Archivo",sans-serif;font-weight:800;font-size:16px;line-height:18px;color:var(--green-text)}
.area.roseville{left:427px;top:32px}
.area.rocklin{left:602px;top:17px}
.area.granite{left:521px;top:54px}
.brand{position:absolute;right:12px;top:9px;font-size:7px;line-height:9px;font-weight:600;color:var(--navy);white-space:nowrap}
.portrait{position:absolute;left:713px;top:30px;width:56px;height:62px;background:linear-gradient(160deg,#8aa35c,#c9a27a)}
.license{position:absolute;left:650px;top:86px;font-size:4.5px;line-height:5px;color:var(--navy)}
.contact-email{position:absolute;left:80px;top:64px;font-size:14px;line-height:16px;color:var(--white)}
.contact-phone{position:absolute;left:100px;top:84px;font-size:6.5px;line-height:8px;color:var(--white)}
.nav-pointer{position:absolute;left:22px;top:96px;width:0;height:0;border-left:8px solid transparent;border-right:8px solid transparent;border-top:8px solid #b9cdea}

.nav{position:absolute;top:119px;left:15px;font-size:8.5px;line-height:10px;color:var(--nav)}
.nav a{color:inherit;text-decoration:none;position:absolute;white-space:nowrap}
.nav a.current{color:var(--white)}

.newsletter{position:absolute;left:0;top:152px;width:774px;height:82px;background:var(--green)}
.newsletter svg{position:absolute;inset:0}
.newsletter h2{position:absolute;left:16px;top:12px;font-size:15px;line-height:18px;font-weight:700;color:var(--white)}
.newsletter p{position:absolute;left:16px;top:37px;width:405px;font-size:9px;line-height:16.5px;color:#9c9c9c}
.signup{position:absolute;left:488px;top:25px;width:206px;height:34px;background:var(--white);border:2px solid #d8d8d8;display:flex;align-items:center;padding-left:12px;gap:14px;font-size:7px;font-weight:600;color:#777}
.go{position:absolute;left:706px;top:25px;width:44px;height:34px;background:var(--tan);border-radius:3px;display:flex;align-items:center;justify-content:center;font-size:10px;font-weight:700;color:var(--ink)}

.features{position:absolute;left:0;top:234px;width:774px;height:400px;background:var(--card-gap)}
.card{position:absolute;top:4px;height:400px;background:var(--white);text-align:center}
.card.c1{left:0;width:255px}
.card.c2{left:258px;width:257px}
.card.c3{left:519px;width:255px;height:341px}
.card h3{position:absolute;left:0;right:0;top:24px;font-size:14.5px;font-weight:600;line-height:20px;color:var(--ink)}
.c1 h3{padding:0 18px}
.c2 h3{padding:0 60px}
.c3 h3{padding:0 26px}
.icon{position:absolute;left:50%;top:92px;width:62px;height:44px;margin-left:-31px;border-radius:6px;background:var(--icon)}
.note{position:absolute;left:24px;top:190px;width:206px;height:72px;border:1px dotted #555;font-size:10px;line-height:18px;color:var(--muted);padding:8px 12px 0}
.note em{font-style:normal;color:#5a7f2a}
.card p.body{position:absolute;left:0;right:0;font-size:10px;line-height:18px;color:var(--muted)}
.c1 p.body{top:280px;padding:0 30px}
.c2 p.body{top:190px;padding:0 24px}
.c3 p.body{top:190px;padding:0 26px}
.btn{position:absolute;left:50%;margin-left:-40px;width:80px;height:26px;line-height:26px;background:var(--green-dark);color:var(--white);font-size:9px;border-radius:2px;box-shadow:0 1px 1px rgba(0,0,0,.3)}
.c1 .btn{top:376px}
.c2 .btn,.c3 .btn{top:289px}
</style>
</head>
<body>
<div class="site">
  <header class="banner">
    <svg width="774" height="96" viewBox="0 0 774 96" aria-hidden="true">
      <defs>
        <linearGradient id="sky" x1="0" y1="0" x2="0" y2="1">
          <stop offset="0" stop-color="#ffffff"/>
          <stop offset=".7" stop-color="#ffffff"/>
          <stop offset="1" stop-color="#9fbbe4"/>
        </linearGradient>
      </defs>
      <rect width="774" height="96" fill="url(#sky)"/>
      <path d="M0 0H250C340 0 400 62 540 80C640 92 720 90 774 88V96H0Z" fill="var(--green)"/>
      <path d="M240 72H297" stroke="#1c2a14" stroke-width="1"/>
    </svg>
    <div class="houses" role="img" aria-label="Line art of house rooftops"></div>
    <div class="areas-label">Areas of service</div>
    <div class="area roseville">Roseville</div>
    <div class="area rocklin">Rocklin</div>
    <div class="area granite">Granite Bay</div>
    <div class="brand">Halverson Realty</div>
    <div class="portrait" role="img" aria-label="Portrait photo of the realtor"></div>
    <div class="license">License # 04729318</div>
    <div class="contact-email">lia@liaporter.com</div>
    <div class="contact-phone">Phone (555)304-2871</div>
  </header>
  <div class="nav-pointer"></div>
  <nav class="nav">
    <a class="current" style="left:0">HOME</a>
    <a style="left:58px">ABOUT</a>
    <a style="left:120px">HOME BUYERS</a>
    <a style="left:214px">HOME SELLERS</a>
    <a style="left:312px">TESTIMONIALS</a>
    <a style="left:407px">CONTACT</a>
  </nav>
  <section class="newsletter">
    <svg width="774" height="82" viewBox="0 0 774 82" aria-hidden="true">
      <path d="M0 0H398L432 41L398 82H0Z" fill="#1f1e1d"/>
      <path d="M0 0H390L424 41L390 82H0Z" fill="var(--band-dark)"/>
    </svg>
    <h2>REAL ESTATE NEWS &amp; RESOURCES</h2>
    <p>Join our readers who receive regular market updates, trends, and Roseville &amp; Rocklin Real estate resources, directly to their inbox...FREE. Don't miss out! Enter your email to the right.</p>
    <div class="signup">
      <svg width="12" height="9" viewBox="0 0 12 9" aria-hidden="true"><rect x=".5" y=".5" width="11" height="8" fill="none" stroke="#aaa"/><path d="M.5 .5L6 5L11.5 .5" fill="none" stroke="#aaa"/></svg>
      ENTER YOUR EMAIL ADDRESS...
    </div>
    <div class="go">GO</div>
  </section>
  <section class="features">
    <article class="card c1">
      <h3>SELL MY HOUSE...SHOW ME THE MONEY!</h3>
      <div class="icon" role="img" aria-label="Handshake icon"></div>
      <div class="note">If you're new here, you may want to subscribe to my <em>RSS feed</em>. Thanks for visiting!</div>
      <p class="body">Not only am I an experienced short sale negotiator, I also apply my skills and experience to the less complicated process of negotiating traditional home sales for my valued clients.</p>
      <span class="btn">LEARN MORE</span>
    </article>
    <article class="card c2">
      <h3>EDUCATIONAL VIDEO LIBRARY</h3>
      <div class="icon" role="img" aria-label="Film strip icon"></div>
      <p class="body">It is important to me that you have all the information you may need to make informed decisions before and during your next real estate transaction. Visit our video library.</p>
      <span class="btn">LEARN MORE</span>
    </article>
    <article class="card c3">
      <h3>12 INDICATORS YOU MAY NEED A SHORT SALE</h3>
      <div class="icon" role="img" aria-label="Light bulb icon"></div>
      <p class="body">Are you unsure if a Short Sale is right for you? How does one know when a short sale is, or should be, an option? Check out these 12 indicators and ask yourself if any apply to you.</p>
      <span class="btn">LEARN MORE</span>
    </article>
  </section>
</div>
</body>
</html>
```